Business Card Design

Take existing logo/brand and develop business card for sales team.
We have two separate brands and require a business card for each.

1. VoxHarbor
2. MyNimbusLinko

Refer to our websites www.voxharbor.example.au and www.mynimbuslinko.example.au for designs currently implemented and in the marketplace.

Both cards are brands of our parent company Quorra Systems Pty Ltd - an Australian Telecommunications company in the medium business sector. We have only business customers, no retail/residential consumers.

Target Market(s)

Australian Business - small to medium enterprise

Industry/Entity Type

Business

Contact Information for Business Card

Lev Dorrit
Sales Director
Mobile: +61 400 555 187
Direct: +61 3 9555 0137
Email: lev@voxharbor.example.au
VoxHarbor (a brand of Quorra Systems Pty Ltd)

Lev Dorrit
Sales Director
Mobile: +61 400 555 187
Direct: +61 3 9555 0137
Email: lev@mynimbuslinko.example.au
MyNimbusLinko (a brand of Quorra Systems Pty Ltd)

Font styles to use
Sans Serif
Other font styles liked:
• Roboto Condensed, Open Sans

Requirements
Must have
• Clean lines, crisp fonts - suggest Roboto Condensed or similar.
• Must be easy to read and clear.
• Brand colour #0C8CCD
• Two colour maximum
Nice to have
• Modern, intellectual and unique design.
Should not have
• No die cuts
• No copies or rip-offs of other designs

```html
<!DOCTYPE html>
<html lang="en">
<head>
<meta charset="utf-8">
<title>VoxHarbor Business Card</title>
<link rel="stylesheet" href="https://fonts.googleapis.com/css2?family=Mulish:wght@800&family=Questrial&family=Poiret+One&display=swap">
<style>
  :root {
    --page-bg: #ffffff;
    --brand-blue: #29abe2;
    --text-blue: #2aaee6;
    --poly-light: #a9def7;
    --poly-mid: #5cc4f0;
    --poly-deep: #31b3ee;
    --card-white: #ffffff;
    --shadow: rgba(0, 0, 0, 0.28);
  }
  * { margin: 0; padding: 0; box-sizing: border-box; }
  html, body {
    width: 1200px;
    height: 1000px;
    overflow: hidden;
    background: var(--page-bg);
  }
  .canvas {
    position: relative;
    width: 1200px;
    height: 1000px;
  }
  .card {
    position: absolute;
    width: 726px;
    height: 424px;
    border-radius: 10px;
    overflow: hidden;
    box-shadow: 0 4px 18px var(--shadow);
  }
  .card--front {
    left: 234px;
    top: 56px;
    background: linear-gradient(125deg, var(--poly-mid) 0%, var(--poly-light) 28%, var(--poly-mid) 48%, var(--poly-deep) 70%, var(--poly-light) 100%);
  }
  .card--back {
    left: 232px;
    top: 522px;
    background: var(--card-white);
  }
  .front-pattern {
    position: absolute;
    inset: 0;
  }
  .brand-lockup {
    position: absolute;
    left: 0;
    right: 0;
    top: 164px;
    display: flex;
    align-items: center;
    justify-content: center;
    gap: 16px;
  }
  .brand-lockup__dot {
    width: 84px;
    height: 84px;
    border-radius: 50%;
    background: var(--card-white);
  }
  .brand-lockup__name {
    font-family: "Questrial", sans-serif;
    font-size: 58px;
    color: var(--card-white);
    line-height: 1;
  }
  .contact {
    position: absolute;
    left: 28px;
    top: 26px;
    color: var(--text-blue);
    font-family: "Questrial", sans-serif;
  }
  .contact__name {
    font-family: "Mulish", sans-serif;
    font-weight: 800;
    font-size: 41px;
    color: var(--brand-blue);
    line-height: 1;
    letter-spacing: 0.5px;
  }
  .contact__title {
    font-size: 16px;
    margin-left: 3px;
    margin-top: 3px;
    line-height: 1;
  }
  .contact__lines {
    list-style: none;
    margin-top: 20px;
    margin-left: 2px;
    font-size: 23px;
    line-height: 30px;
  }
  .back-band {
    position: absolute;
    inset: 0;
  }
  .company-line {
    position: absolute;
    right: 12px;
    bottom: 12px;
    font-family: "Poiret One", sans-serif;
    font-size: 29px;
    color: var(--card-white);
    line-height: 1;
  }
</style>
</head>
<body>
<main class="canvas">

  <section class="card card--front" aria-label="Card front">
    <svg class="front-pattern" role="img" aria-label="Faceted low-poly pattern in light and mid blues" width="726" height="424" viewBox="0 0 726 424">
      <defs>
        <radialGradient id="frontGlow" cx="0.72" cy="0.7" r="0.55">
          <stop offset="0" stop-color="#d4eefb" stop-opacity="0.7"/>
          <stop offset="1" stop-color="#d4eefb" stop-opacity="0"/>
        </radialGradient>
      </defs>
      <rect width="726" height="424" fill="url(#frontGlow)"/>
    </svg>
    <div class="brand-lockup">
      <span class="brand-lockup__dot"></span>
      <span class="brand-lockup__name">VoxHarbor</span>
    </div>
  </section>

  <section class="card card--back" aria-label="Card back">
    <svg class="back-band" width="726" height="424" viewBox="0 0 726 424" aria-hidden="true">
      <defs>
        <linearGradient id="bandFill" x1="0.1" y1="1" x2="1" y2="0.2">
          <stop offset="0" stop-color="#b4e2f8"/>
          <stop offset="0.45" stop-color="#6ccaf2"/>
          <stop offset="1" stop-color="#31b3ee"/>
        </linearGradient>
        <filter id="bandShadow" x="-10%" y="-10%" width="120%" height="120%">
          <feDropShadow dx="0" dy="-2" stdDeviation="3" flood-color="#000" flood-opacity="0.2"/>
        </filter>
      </defs>
      <polygon role="img" aria-label="Diagonal band with faceted blue pattern" points="138,424 726,96 726,424" fill="url(#bandFill)" filter="url(#bandShadow)"/>
    </svg>

    <div class="contact">
      <h1 class="contact__name">Lev Dorrit</h1>
      <p class="contact__title">Sales Director</p>
      <ul class="contact__lines">
        <li>Mobile: +61 400 555 187</li>
        <li>Direct: +61 3 9555 0137</li>
        <li>Email: lev@voxharbor.example.au</li>
      </ul>
    </div>

    <p class="company-line">Quorra Systems Pty Ltd</p>
  </section>

</main>
</body>
</html>
```